Holiday/6-Mo. Firm Anniversary Graphic for E-mail to Clients

Here is the proposed text:
2 Reasons to Celebrate:
Happy New Year 2024
&
The 6-Month Anniversary
Of
Draven Law Offices
Focusing on Commercial Litigation,
Real Estate,Telecom and Healthcare
Disputes
I think what I would like is a static graphic that would be something that I send to
clients celebrating my law firm’s 6-month anniversary (around the first of the year so a New Year theme could be incorporated maybe). Maybe something with a picture of my face along with a cartoon/graphic body of me doing something lawyerly. Something simple but unique and maybe humorous. Then something referencing the 6-month anniversary. I don’t anything like sound or sound effect. I am not very creative, sorry. Attached are a few headshots we might use.
Target Market(s)
Current clients and future clients with prior relationships
Look and feel

```html
<!DOCTYPE html>
<html lang="en">
<head>
<meta charset="utf-8">
<title>Draven Reed Law Firm – 6 Month Anniversary</title>
<link rel="stylesheet" href="https://fonts.googleapis.com/css2?family=Cinzel:wght@700&family=Playfair+Display:wght@900&family=Oswald:wght@600&family=Dancing+Script:wght@700&display=swap">
<style>
  :root {
    --sky-light: #f4f8fe;
    --sky-mid: #dce9f8;
    --sky-deep: #c4daf2;
    --ink: #111111;
    --accent-red: #c8141c;
    --band-red: #c3161e;
    --band-dark: #8a0d13;
    --gold-light: #fff0a0;
    --gold-mid: #e3b23a;
    --gold-deep: #a8741a;
    --balloon-tone: #e7b7cb;
    --balloon-tone-2: #b5cff0;
    --figure-tone: #2b2b2d;
    --figure-tone-2: #3c3a3a;
    --white: #ffffff;
  }
  * { margin: 0; padding: 0; box-sizing: border-box; }
  html, body { width: 1200px; height: 1000px; overflow: hidden; }
  body { background: var(--white); }

  .card {
    position: relative;
    width: 1200px;
    height: 1000px;
    overflow: hidden;
    background: radial-gradient(circle at 33% 30%, var(--sky-light) 0%, var(--sky-light) 25%, var(--sky-mid) 65%, var(--sky-deep) 100%);
  }

  .balloon-area {
    position: absolute;
    border-radius: 40px;
    opacity: 0.55;
  }
  .balloon-area--right {
    left: 900px; top: 0; width: 300px; height: 600px;
    background: linear-gradient(180deg, var(--balloon-tone-2), var(--balloon-tone));
    border-radius: 0 0 0 60px;
  }
  .balloon-area--bottom {
    left: 0; top: 760px; width: 660px; height: 240px;
    background: linear-gradient(90deg, var(--balloon-tone), var(--balloon-tone-2));
    border-radius: 0 60px 0 0;
  }

  .milestone-number {
    position: absolute;
    left: 240px; top: 20px;
    width: 200px;
    text-align: center;
    font-family: "Playfair Display", serif;
    font-weight: 900;
    font-size: 330px;
    line-height: 1;
    background: linear-gradient(160deg, var(--gold-light) 0%, var(--gold-mid) 40%, var(--gold-deep) 75%, var(--gold-mid) 100%);
    -webkit-background-clip: text;
    background-clip: text;
    color: transparent;
  }

  .month-tag {
    position: absolute;
    left: 410px; top: 292px;
    padding: 0 20px;
    height: 72px;
    line-height: 72px;
    background: var(--band-dark);
    font-family: "Dancing Script", cursive;
    font-weight: 700;
    font-size: 54px;
    color: var(--white);
  }
  .anniversary-band {
    position: absolute;
    left: 110px; top: 352px;
    width: 460px; height: 84px;
    background: var(--band-red);
    text-align: center;
    line-height: 84px;
    font-family: "Oswald", sans-serif;
    font-weight: 600;
    font-size: 52px;
    letter-spacing: 1px;
    color: var(--white);
  }

  .firm-name {
    position: absolute;
    left: 40px; top: 494px;
    width: 640px;
    text-align: center;
    font-family: "Cinzel", serif;
    font-weight: 700;
    color: var(--ink);
    line-height: 1;
  }
  .firm-name__primary { display: block; font-size: 68px; }
  .firm-name__secondary { display: block; margin-top: 22px; font-size: 50px; }

  .occasion {
    position: absolute;
    left: 30px; top: 676px;
    width: 660px;
    text-align: center;
    font-family: "Cinzel", serif;
    font-weight: 700;
    font-size: 64px;
    color: var(--accent-red);
    line-height: 1;
  }

  .attorney-figure {
    position: absolute;
    left: 640px; top: 160px;
    width: 540px; height: 820px;
    border-radius: 36px;
    background: linear-gradient(180deg, var(--figure-tone), var(--figure-tone-2));
  }
</style>
</head>
<body>
  <main class="card">
    <div class="balloon-area balloon-area--right" role="img" aria-label="Cluster of festive party balloons"></div>
    <div class="balloon-area balloon-area--bottom" role="img" aria-label="Row of festive party balloons along the bottom"></div>

    <div class="milestone-number">6</div>
    <div class="month-tag">Month</div>
    <div class="anniversary-band">ANNIVERSARY</div>

    <h1 class="firm-name">
      <span class="firm-name__primary">Draven Reed</span>
      <span class="firm-name__secondary">Law Firm</span>
    </h1>
    <p class="occasion">ANNIVERSARY</p>

    <div class="attorney-figure" role="img" aria-label="Caricature of the attorney in a dark suit and red tie holding a thick folder of case files"></div>
  </main>
</body>
</html>
```